Label Design for Cook Marsh Kimchi Sauce – Modern Korean Fermentation Brand

We are developing the primary packaging identity for COOK MARSH, beginning with our flagship Korean Kimchi Sauce.
Cook Marsh is a contemporary Korean food brand built around an idea that is central to Korean cuisine: Tradition refined through modern food science. Our kimchi sauce is not intended to be simply another spicy Korean condiment, but rooted in authentic Korean kimchi fermentation and combines traditional fermentation knowledge with modern process control to create a consistent, flavorful and convenient shelf-stable sauce.
The goal of this project is to create a distinctive, typography-led master label and visual identity that can eventually expand across an entire Cook Marsh product family. The winning design should feel credible as the beginning of a serious international food brand, rather than as a one-off sauce label.
This first project is for our Kimchi Sauce bottle and Kimchi Paste package, but the design should establish a master brand system that can later expand into additional products such as Korean Kimchi Sauce and Korean Kimchi Paste.
Primary sauce bottle is approximately:
300 mL / 10.1 FL OZ
The label design should be developed specifically with the proportions, readability and shelf presence of a 300 mL sauce bottle in mind.
We want the design to place much greater emphasis on text, font, typography and brand hierarchy than on graphics or illustration. Should be driven primarily by distinctive typography, strong font selection or custom lettering, clear hierarchy, strong use of scale and proportion, memorable wordmark treatment, spacing and composition, recognizable label structure, with Cook Marsh and Kimchi Sauce as the visual focus. Graphics and illustrations can be used, but they should be secondary and restrained, not the main feature of the package.
A brand such as Verluna, particularly its 300 mL bottle presentation, is useful as a general reference for the importance of typography, simplicity, hierarchy, shelf recognition and longevity. We are not looking to copy Verluna's design, but we appreciate how strongly the brand is communicated through text and label structure rather than decorative graphics.
The brand concept combines:
• Korean fermentation heritage
• modern scientific precision
• real food / plant-forward ingredients
• global culinary versatility
Front Label Priorities
The front label should clearly communicate:
1. COOK MARSH as the master brand
2. KIMCHI SAUCE as the product
3. 300 mL / 10.1 FL OZ
4. A premium, clean and modern aesthetic
5. An appetizing and confident Korean identity
Possible supporting themes or optional secondary messaging:
• Authentically Fermented
• Crafted for Consistency
• Korean Chili Blend
• Bold & Tangy
• Tradition Refined by Science
These are secondary messages only. We prefer strong typography and hierarchy over excessive front-label copy. We are open to creative exploration, but the design should feel typography-led, modern, premium, bold, clean, warm, appetizing, rooted in Korean heritage, recognizable from a distance, scalable across future products
Please keep graphics minimal and secondary.
Ingredient illustrations such as cabbage, chili peppers, garlic or herbs may be used if they support the design, but they should not dominate the label.
Our preliminary concepts use more ingredient illustration than we ultimately want. We are sharing them as a starting point, but we would like designers to move the brand toward a cleaner, stronger and more typography-focused identity.
A strong concept should still work even if most decorative graphics were removed.
Please avoid:
• illustration-heavy labels
• overly busy ingredient graphics
• overly rustic packaging
• typography that feels generic or secondary
• copycat designs of existing trendy sauce brands
The final design should make the consumer remember COOK MARSH, not simply the pictures on the bottle.

```html
<!DOCTYPE html>
<html lang="en">
<head>
<meta charset="utf-8">
<title>Cook Marsh Kimchi Sauce – Front Label</title>
<link rel="stylesheet" href="https://fonts.googleapis.com/css2?family=Bebas+Neue&family=Bungee&family=Oswald:wght@500;600&display=swap">
<style>
  :root {
    --page: #f7f5f2;
    --label-black: #0b0a0a;
    --brand-red: #d9141e;
    --chili-yellow: #f6ab1d;
    --blossom-pink: #ec62a2;
    --ember-orange: #f2661f;
  }
  * { box-sizing: border-box; margin: 0; padding: 0; }
  html, body {
    width: 1200px;
    height: 1200px;
    overflow: hidden;
    background: var(--page);
  }
  .canvas {
    position: relative;
    width: 1200px;
    height: 1200px;
  }
  .front-label {
    position: absolute;
    left: 370px;
    top: 58px;
    width: 460px;
    height: 1084px;
    background: var(--label-black);
    border-radius: 150px 150px 70px 70px / 130px 130px 60px 60px;
    text-align: center;
  }
  .front-label > * {
    position: absolute;
    left: 0;
    right: 0;
  }
  .brand-name {
    top: 160px;
    font-family: "Bebas Neue", sans-serif;
    font-size: 88px;
    line-height: 1;
    letter-spacing: 1px;
    color: var(--brand-red);
  }
  .blossom-emblem {
    top: 262px;
    left: 85px;
    width: 290px;
    height: 316px;
    border-radius: 50% 50% 45% 45%;
    background: radial-gradient(circle at 50% 35%, var(--blossom-pink) 0%, var(--ember-orange) 55%, var(--chili-yellow) 100%);
    opacity: 0.9;
  }
  .leaf-accent {
    top: 604px;
    left: 200px;
    width: 60px;
    height: 72px;
    border-radius: 50% 50% 50% 50% / 60% 60% 40% 40%;
    background: linear-gradient(135deg, var(--ember-orange), var(--blossom-pink));
  }
  .product-name {
    top: 722px;
    font-family: "Bungee", sans-serif;
    font-size: 76px;
    line-height: 0.98;
    color: var(--chili-yellow);
  }
  .product-descriptor {
    top: 936px;
    font-family: "Oswald", sans-serif;
    font-weight: 600;
    font-size: 30px;
    letter-spacing: 0.5px;
    color: var(--brand-red);
  }
  .net-volume {
    top: 1012px;
    font-family: "Oswald", sans-serif;
    font-weight: 500;
    font-size: 23px;
    letter-spacing: 0.5px;
    color: var(--brand-red);
  }
  .net-volume .divider { padding: 0 8px; }
</style>
</head>
<body>
  <main class="canvas">
    <section class="front-label">
      <h1 class="brand-name">COOK MARSH</h1>
      <div class="blossom-emblem" role="img" aria-label="Stylised chili blossom emblem in pink, orange and yellow"></div>
      <div class="leaf-accent" role="img" aria-label="Small pair of orange and pink leaves"></div>
      <h2 class="product-name">KIMCHI<br>SAUCE</h2>
      <p class="product-descriptor">KOREAN CHILI BLEND</p>
      <p class="net-volume">300ML<span class="divider">|</span>10.1 FL. OZ.</p>
    </section>
  </main>
</body>
</html>
```